Marlo's Bakes Tortehouse LLC website

Artisan cheesecake business looking for excellent talent to design bright, fun, engaging website for our company. We also recently acquired a food truck so we are able to cater and attend food truck events.
Our mission is to create fun, unique, delicious flavors of cheesecake and we bake them in mason jars and whole cheesecakes. We strive to exceed our customers' expectations in everything we do.
Target Market(s)
Foodies, cheesecake lovers, dessert lovers, food truck people,
Industry/Entity Type
Dessert, Catering, Pop Up events, Food truck
Coding
Coded - Design and coding required
Number of Pages Required
4 page
Requirements
Must have
- Pictures of my cheesecakes
Nice to have
- Bright, colorful, eye-catching design with a good flow

```html
<!DOCTYPE html>
<html lang="en">
<head>
<meta charset="utf-8">
<title>Marlo's Bakes – Artisan Cheesecakes</title>
<link href="https://fonts.googleapis.com/css2?family=Lato:wght@400;700&family=Pacifico&display=swap" rel="stylesheet">
<style>
:root{
  --pink:#f4a3b6;
  --pink-soft:#f7b6c5;
  --pink-pale:#fbe0e6;
  --pink-deep:#e8919f;
  --ink:#222;
  --text:#444;
  --grey-bg:#f2f2f2;
  --field:#f1f1f1;
  --white:#fff;
  --black:#000;
}
*{box-sizing:border-box;margin:0;padding:0}
html,body{width:1200px;height:3594px;overflow:hidden}
body{position:relative;font-family:'Lato',sans-serif;color:var(--text);background:var(--white)}
.abs{position:absolute}
.script{font-family:'Pacifico',cursive;font-weight:400}
.btn{position:absolute;display:flex;align-items:center;justify-content:center;background:var(--pink);color:var(--white);border-radius:40px;font-family:'Pacifico',cursive;font-size:17px}
.photo{position:absolute}

/* header */
.topbar{left:541px;top:0;width:547px;height:43px;background:var(--pink);border-radius:0 0 22px 22px;display:flex;align-items:center;justify-content:space-around;color:var(--white);font-size:15px;padding:0 20px}
.topbar span{display:flex;align-items:center;gap:8px}
.nav{left:468px;top:62px;display:flex;gap:54px;font-size:16px;color:var(--ink)}
.nav .active{color:var(--pink);border-bottom:2px solid var(--pink);padding-bottom:6px}
.logo{left:120px;top:3px;width:162px;height:162px;border-radius:50%;background:var(--pink);border:7px solid var(--white);display:flex;align-items:center;justify-content:center;color:var(--white);font-size:19px;font-weight:700;z-index:3;text-align:center}

/* hero */
.hero{left:0;top:103px;width:1200px;height:622px;background:linear-gradient(180deg,#f6b3c2,#f4a9ba)}
.hero h1{position:absolute;left:110px;top:200px;font-size:37px;line-height:1.3;white-space:nowrap;color:var(--white);z-index:2}
.hero p{position:absolute;left:110px;top:276px;width:440px;font-size:15px;line-height:26px;color:var(--white)}
.hero .btn{left:110px;top:345px;width:154px;height:57px;background:var(--white);color:var(--pink)}
.hero-ring{left:621px;top:191px;width:468px;height:468px;border-radius:50%;background:var(--pink-pale);opacity:.85}
.hero-photo{left:645px;top:215px;width:420px;height:420px;border-radius:50%;background:radial-gradient(circle at 40% 40%,#e9d2a8,#c89a62 60%,#b77a87)}

/* products */
.section-title{position:absolute;width:1200px;text-align:center;font-size:36px;color:var(--ink)}
.card{position:absolute;top:960px;width:232px;height:271px;background:var(--white);border-radius:12px;box-shadow:0 4px 18px rgba(0,0,0,.08)}
.card-photo{position:absolute;top:889px;width:208px;height:190px;border-radius:12px}
.card-name{position:absolute;top:1092px;width:232px;text-align:center;font-size:22px;color:var(--ink)}
.card-price{position:absolute;top:1140px;width:232px;text-align:center;font-size:15px;color:var(--pink)}
.card-price s{color:#ccc;margin-left:8px}
.card .btn{left:59px;top:216px;width:114px;height:41px;font-size:14px}

/* about */
.about{left:0;top:1313px;width:1200px;height:543px;background:var(--grey-bg)}
.about-ring{left:114px;top:1369px;width:412px;height:412px;border-radius:50%;background:var(--pink-pale)}
.about-photo{left:137px;top:1392px;width:366px;height:366px;border-radius:50%;background:radial-gradient(circle at 50% 50%,#a5242e,#7a1c24 45%,#3c5a2e)}
.about h2{position:absolute;left:573px;top:95px;font-size:36px;color:var(--ink)}
.about p{position:absolute;left:575px;top:160px;width:512px;font-size:15px;line-height:25.8px;color:var(--ink)}
.about .btn{left:576px;top:385px;width:153px;height:57px}

/* gallery */
.gallery{left:0;top:1856px;width:1200px;height:659px;background:linear-gradient(180deg,#eb97a7,#e58e9e)}
.gallery h2{position:absolute;width:1200px;top:48px;text-align:center;font-size:36px;color:var(--white)}
.frame{position:absolute;background:var(--white);padding:8px}
.frame div{width:100%;height:100%}
.g-caption{position:absolute;left:453px;top:2350px;width:300px;height:78px;background:var(--pink-soft);display:flex;align-items:center;justify-content:center;color:var(--white);font-size:28px}
.arrow{position:absolute;width:30px;height:30px;border-radius:50%;display:flex;align-items:center;justify-content:center}

/* contact */
.contact-intro{position:absolute;left:220px;top:2665px;width:760px;text-align:center;font-size:15px;line-height:26px;color:var(--text)}
.field{position:absolute;background:var(--field);font-size:15px;color:#777;padding:16px 28px}
.touch h3{position:absolute;left:742px;top:2770px;font-size:26px;color:var(--ink)}
.touch-item{position:absolute;left:748px;display:flex;gap:18px;font-size:15px;line-height:26px;color:var(--ink)}
.social{position:absolute;top:2998px;width:40px;height:40px;border-radius:50%;border:1.5px solid var(--pink)}

/* footer */
.footer{left:0;top:3202px;width:1200px;height:392px;background:var(--black);color:var(--white)}
.f-logo{position:absolute;left:135px;top:63px;width:202px;height:202px;border-radius:50%;background:var(--pink);display:flex;align-items:center;justify-content:center;font-size:22px;font-weight:700;text-align:center}
.f-col h4{position:absolute;top:70px;font-family:'Pacifico',cursive;font-weight:400;font-size:22px}
.f-col ul{position:absolute;top:120px;list-style:none;font-size:15px}
.f-col li{height:30.5px}
.f-col li::before{content:"«";margin-right:12px}
.f-input{position:absolute;left:808px;top:125px;width:272px;height:41px;border:1px solid #888;border-radius:22px;padding:11px 18px;font-size:14px;color:#999}
.f-btn{left:808px;top:177px;width:272px;height:40px}
.f-rule{position:absolute;left:108px;top:299px;width:984px;height:1px;background:#333}
.copy{position:absolute;top:334px;width:1200px;text-align:center;font-size:15px}
</style>
</head>
<body>

<!-- header -->
<div class="abs topbar">
  <span><svg width="16" height="16" viewBox="0 0 24 24" fill="#fff"><path d="M6.6 10.8a15 15 0 0 0 6.6 6.6l2.2-2.2a1 1 0 0 1 1-.25 11.4 11.4 0 0 0 3.6.57 1 1 0 0 1 1 1V20a1 1 0 0 1-1 1A17 17 0 0 1 3 4a1 1 0 0 1 1-1h3.5a1 1 0 0 1 1 1c0 1.25.2 2.45.57 3.57a1 1 0 0 1-.25 1z"/></svg>+1 888 888 8888</span>
  <span><svg width="16" height="14" viewBox="0 0 24 20" fill="#fff"><path d="M2 2h20v16H2z" opacity=".95"/><path d="M2 2l10 8 10-8" stroke="#f4a3b6" stroke-width="2" fill="none"/></svg>info@marlosbakes.com</span>
  <span><svg width="14" height="14" viewBox="0 0 24 24" fill="#fff"><path d="M10 17l5-5-5-5v3H2v4h8zM14 3h6a2 2 0 0 1 2 2v14a2 2 0 0 1-2 2h-6v-2h6V5h-6z"/></svg>Login</span>
</div>
<nav class="abs nav">
  <span class="active">Home</span><span>About Us</span><span>OurProducts</span><span>How it Work</span><span>Contact Us</span>
</nav>
<div class="abs logo">Marlo's Bakes</div>

<!-- hero -->
<section class="abs hero">
  <h1 class="script">Welcome To Marlo's Bakes</h1>
  <p>Lorem ipsum dolor sit amet, consectetur adipiscing elit, sed do eiusmod tempor incididunt ut labore et dolore</p>
  <div class="btn">Learn More</div>
</section>
<div class="abs hero-ring"></div>
<div class="photo hero-photo" role="img" aria-label="Slices of assorted cheesecakes with branded stickers"></div>

<!-- products -->
<h2 class="section-title script" style="top:800px">Our Products</h2>

<div class="card" style="left:98px"><div class="btn">Add To Cart</div></div>
<div class="card" style="left:355px"><div class="btn">Add To Cart</div></div>
<div class="card" style="left:611px"><div class="btn">Add To Cart</div></div>
<div class="card" style="left:868px"><div class="btn">Add To Cart</div></div>

<div class="card-photo" role="img" aria-label="Strawberry topped caramel cheesecake" style="left:110px;background:linear-gradient(160deg,#c8302a,#d9733a 55%,#e6c98a)"></div>
<div class="card-photo" role="img" aria-label="Banana cream cheesecake with wafers" style="left:367px;background:linear-gradient(160deg,#f1e6c8,#c98e4e 60%,#8d5a2b)"></div>
<div class="card-photo" role="img" aria-label="Slice of banana layer cheesecake" style="left:623px;background:linear-gradient(160deg,#4f5a3e,#e3c79b 50%,#f4ecd8)"></div>
<div class="card-photo" role="img" aria-label="Strawberry layer cheesecake slice" style="left:880px;background:linear-gradient(160deg,#4c6a36,#e8777d 50%,#f3d9d2)"></div>

<div class="card-name script" style="left:98px">Marlo's Bakes</div>
<div class="card-name script" style="left:355px">Marlo's Bakes</div>
<div class="card-name script" style="left:611px">Marlo's Bakes</div>
<div class="card-name script" style="left:868px">Marlo's Bakes</div>
<div class="card-price" style="left:98px">$300.00<s>$450.00</s></div>
<div class="card-price" style="left:355px">$300.00<s>$450.00</s></div>
<div class="card-price" style="left:611px">$300.00<s>$450.00</s></div>
<div class="card-price" style="left:868px">$300.00<s>$450.00</s></div>

<!-- about -->
<section class="abs about">
  <h2 class="script">About Us</h2>
  <p>Lorem ipsum dolor sit amet, consectetur adipiscing elit, sed do eiusmod tempor incididunt ut labore et dolore magna aliqua. Quis ipsum suspendisse ultrices gravida. Risus commodo viverra maecenas accumsan lacus vel facilisis. Lorem ipsum dolor sit amet, consectetur adipiscing elit, sed do eiusmod tempor incididunt ut labore et dolore magna aliqua. Quis ipsum suspendisse ultrices gravida. Risus commodo viverra maecenas accumsan lacus vel facilisis. Lorem ipsum dolor sit amet, consectetur adipiscing elit, sed do eiusmod tempor incididunt</p>
  <div class="btn">Learn More</div>
</section>
<div class="abs about-ring"></div>
<div class="photo about-photo" role="img" aria-label="Slice of red velvet cheesecake on a plate"></div>

<!-- gallery -->
<section class="abs gallery">
  <h2 class="script">Our Gallery</h2>
</section>
<div class="frame" style="left:176px;top:2050px;width:138px;height:334px"><div role="img" aria-label="Cheesecake being torched" style="background:linear-gradient(180deg,#5a4030,#c46a3a,#8a7a6a)"></div></div>
<div class="frame" style="left:898px;top:2050px;width:138px;height:334px"><div role="img" aria-label="Food truck delivery box" style="background:linear-gradient(180deg,#9a8a70,#4a4440)"></div></div>
<div class="frame" style="left:304px;top:2023px;width:160px;height:380px"><div role="img" aria-label="Red velvet cheesecake slice" style="background:linear-gradient(180deg,#3c5a2e,#a5242e 55%,#e8e4de)"></div></div>
<div class="frame" style="left:745px;top:2030px;width:160px;height:370px"><div role="img" aria-label="Cookies and cream cheesecake jars" style="background:linear-gradient(180deg,#2a4a8a,#d8c8a8 50%,#5a4a3a)"></div></div>
<div class="frame" style="left:445px;top:2003px;width:316px;height:433px"><div role="img" aria-label="Passion fruit cheesecake slices" style="height:336px;background:linear-gradient(180deg,#4a3a4a,#e8a02a 55%,#f2e3b0)"></div></div>
<div class="g-caption script">Marlo's Bakes</div>
<div class="arrow" style="left:161px;top:2204px;background:var(--pink)"><svg width="10" height="10" viewBox="0 0 10 10"><path d="M7 1L3 5l4 4" stroke="#fff" stroke-width="1.6" fill="none"/></svg></div>
<div class="arrow" style="left:1021px;top:2204px;background:var(--white)"><svg width="10" height="10" viewBox="0 0 10 10"><path d="M3 1l4 4-4 4" stroke="#555" stroke-width="1.6" fill="none"/></svg></div>

<!-- contact -->
<h2 class="section-title script" style="top:2588px">Contact Us</h2>
<p class="contact-intro">Lorem ipsum dolor sit amet, consectetur adipiscing elit, sed do eiusmod tempor incididunt ut labore et dolore magna aliqua. Quis ipsum suspendisse ultrices gravida.</p>
<div class="field" style="left:138px;top:2759px;width:254px;height:52px">First Name</div>
<div class="field" style="left:410px;top:2759px;width:254px;height:52px">Late Name</div>
<div class="field" style="left:138px;top:2828px;width:254px;height:52px">Email</div>
<div class="field" style="left:410px;top:2828px;width:254px;height:52px">Phone</div>
<div class="field" style="left:138px;top:2896px;width:526px;height:140px">Messages</div>
<div class="btn" style="left:137px;top:3061px;width:135px;height:56px">Submit</div>

<div class="touch">
  <h3 class="script">Get in Touch</h3>
  <div class="touch-item" style="top:2833px"><svg width="16" height="20" viewBox="0 0 16 20"><path d="M8 0a7 7 0 0 0-7 7c0 5 7 13 7 13s7-8 7-13a7 7 0 0 0-7-7zm0 10a3 3 0 1 1 0-6 3 3 0 0 1 0 6z" fill="#f4a3b6"/></svg><span>199 /b Marlo's Bakes consectetur adipiscing<br>elit, sed do eiusmod tempor</span></div>
  <div class="touch-item" style="top:2898px"><svg width="18" height="18" viewBox="0 0 24 24" fill="#f4a3b6"><path d="M6.6 10.8a15 15 0 0 0 6.6 6.6l2.2-2.2a1 1 0 0 1 1-.25 11.4 11.4 0 0 0 3.6.57 1 1 0 0 1 1 1V20a1 1 0 0 1-1 1A17 17 0 0 1 3 4a1 1 0 0 1 1-1h3.5a1 1 0 0 1 1 1c0 1.250.2 2.45.57 3.57a1 1 0 0 1-.25 1z"/></svg><span>+1 888 888 8888</span></div>
  <div class="touch-item" style="top:2940px"><svg width="18" height="14" viewBox="0 0 24 20"><path d="M2 2h20v16H2z" fill="#f4a3b6"/><path d="M2 2l10 8 10-8" stroke="#fff" stroke-width="2" fill="none"/></svg><span>info@marlosbakes.com</span></div>
  <div class="social" style="left:745px;background:var(--pink)"></div>
  <div class="social" style="left:792px"></div>
  <div class="social" style="left:841px"></div>
  <div class="social" style="left:891px"></div>
</div>

<!-- footer -->
<footer class="abs footer">
  <div class="f-logo">Marlo's Bakes</div>
  <div class="f-col"><h4 style="left:403px">Quick Link</h4>
    <ul style="left:405px"><li>Home</li><li>About Us</li><li>OurProducts</li><li>How it Work</li><li>Contact Us</li></ul></div>
  <div class="f-col"><h4 style="left:593px">Help Link</h4>
    <ul style="left:595px"><li>Terms&amp;condtions</li><li>Privacy Policy</li><li>About Us</li><li>Support</li></ul></div>
  <div class="f-col"><h4 style="left:808px">Get Our Newsletter</h4></div>
  <div class="f-input">Enter Your Email</div>
  <div class="btn f-btn">Subscribe Now</div>
  <div class="f-rule"></div>
  <p class="copy">©Copyrights 2022 Marlo's Bakes | &nbsp; All Rights Reserved</p>
</footer>

</body>
</html>
```